Consulting & Education Company Needs Dynamic MS Word Template

We need a MS Word Template for everyday documents. This would be leveraged to create reports, marketing materials, internal memos etc.

The document should follow the standard MS Word template format and have an H1,H2,H3, paragraph, Title, bold font, regular font, table etc. All editable with normal MS Word features.

Attached is a Logo which was created by one of the many talented folks here at ArtHarbor. We would like to see the same color scheme used throughout the document. Additional attached is a sample word document that outlines all of the components we would like to see in the template.

Target Market(s)

Information Security - Penetration Testing - IT - Network/Systems Engineering

Industry/Entity Type

Education

Requirements
Must have
• Submission must meet all standard MS Word Template requirements.
• Submission should make use of Built in MS Styles so as the user of the template I shoudl be able to create a brand new page and insert an H1 for example and be able to select from the styles drop down the same font/color/style that you have designed for your submission.
• All sections in the provided document need to be contained in your submission.
• The table of contents should auto update if I add a new page, heading, section etc.
• Need to read and understand all of my comments which I have placed in the sample document uploaded to the briefing
Nice to have
• the cover page should be eye catching but not over the top. Some cool vectors/bg colors etc that look nice with the logo already provided.
• Icons and vectors whever they make sense and are visually appealing. For example the document has a section for defiing severity risk: Critical, High, Medium and Low it would be great if there was a nice icon or 2d graphic associated with each one. also color coded is a plus High is more dangerous then medium so the colors should communicate that.
Should not have
• no fixed textboxes or image boxes. everything needs to be smoothly editable in MS Word. "Editable" means more than just being able to alter text.

```html
<!DOCTYPE html>
<html lang="en">
<head>
<meta charset="utf-8">
<title>ProbeWorks Report Template</title>
<link href="https://fonts.googleapis.com/css2?family=Carlito:wght@400;700&family=Gelasio:wght@400;700&display=swap" rel="stylesheet">
<style>
:root{
  --red:#c0262c;
  --red-soft:#c9504f;
  --ink:#222;
  --muted:#9a9a9a;
  --grid:#b8b8b8;
  --panel:#e4e5e4;
  --orange:#ee7b22;
  --yellow:#f3c51b;
  --green:#3fae3f;
  --link:#3a4a9a;
}
*{box-sizing:border-box;margin:0;padding:0}
html,body{width:1200px;height:1200px;overflow:hidden;background:#fff}
body{position:relative;font-family:"Carlito",sans-serif;color:var(--ink)}
.page{position:absolute;width:270px;height:356px;background:#fff;border:1px solid var(--grid);padding:37px 25px 0 23px;overflow:hidden}
.brand{position:absolute;top:13px;left:22px;display:flex;align-items:center;gap:2px;font:700 7px "Carlito",sans-serif;color:var(--muted);letter-spacing:.1px}
.brand i{width:6px;height:6px;background:var(--muted);display:block}
.pnum{position:absolute;top:20px;right:22px;font-size:4.6px}
.foot{position:absolute;bottom:13px;left:23px;font-size:4.6px}
h2{font:700 7.4px "Gelasio",serif;color:var(--red);text-align:center;margin:0 0 5px}
h2.left{text-align:left}
h3{font:700 6px "Gelasio",serif;color:var(--red);text-align:center;margin:8px 0 4px}
h3.dark{color:var(--ink)}
p{font-size:5px;line-height:9.6px}
.sev{text-align:center;font:700 4.8px "Carlito",sans-serif;margin:6px 0 2px}
.sev svg{display:block;margin:3px auto 5px}
.data{width:100%;border-collapse:collapse;font-size:4.6px;font-weight:700;margin:4px 0 8px;border:1px solid var(--red-soft)}
.data caption{background:var(--red-soft);color:#fff;font:700 5.6px "Carlito",sans-serif;padding:2px 0}
.data td{border-top:1px solid var(--red-soft);padding:2px 3px;height:10px}
.data td+td{border-left:1px solid var(--red-soft);text-align:center}
.data.summary td+td{text-align:left}
.data.summary th{text-align:left;padding:2px 3px;font-size:4.6px}
.data.summary th+th{color:var(--red)}
.toc h2{text-align:left;margin-bottom:20px}
.toc li{list-style:none;display:flex;align-items:baseline;font-size:4.4px;height:9.8px}
.toc li .dots{flex:1;border-bottom:0.6px dotted #666;margin:0 1px}
.toc .l2{padding-left:6px}
.toc .l3{padding-left:11px}
.toc .sub{color:var(--link)}
.toc .b{font-weight:700}
.finding{width:229px;border-collapse:collapse;border:1px solid #555;font-size:4.8px;margin:0 auto}
.finding th.title{background:var(--panel);font:700 6px "Gelasio",serif;padding:4px 0;text-align:center;border-bottom:1px solid #555}
.finding td{vertical-align:top;padding:2px 3px;line-height:9.4px;background:var(--panel);border-top:1px solid #555}
.finding td.k{width:53px;font:700 4.8px "Gelasio",serif;border-right:1px solid #555}
.finding td.issue{background:#fff;font:700 4.6px "Gelasio",serif}
.finding td.icon{background:#fff;border-left:1px solid #555;width:54px}
.shot{width:148px;height:112px;margin:2px auto 2px;background:linear-gradient(180deg,#f0f0f0 0,#f0f0f0 12%,#fff 12%,#fff 100%);border:0.5px solid #ccc}
.caption{font-weight:700;font-size:4.4px}
.cover-band{position:absolute;left:2px;top:116px;width:293px;height:17px;background:var(--red);border-top:3px solid #222;border-bottom:3px solid #222}
.cover-logo{position:absolute;top:46px;left:25px;display:flex;align-items:center;gap:5px;font:700 22px "Carlito",sans-serif;color:var(--red)}
.cover-logo i{width:24px;height:24px;background:var(--red);display:block}
.cover h1{position:absolute;top:107px;left:0;width:100%;text-align:center;font:700 11.5px "Gelasio",serif;text-decoration:underline}
.cover .client{position:absolute;top:127px;width:100%;left:0;text-align:center;font:700 7.5px "Gelasio",serif}
.cover .date{position:absolute;top:143px;width:100%;left:0;text-align:center;font:700 6.8px "Gelasio",serif}
.cover .art{position:absolute;top:162px;left:59px;width:152px;height:150px;background:radial-gradient(circle at 45% 45%,#d8d8d8,#f4f4f4 70%,#fff)}
</style>
</head>
<body>

<svg width="0" height="0" style="position:absolute">
  <defs>
    <symbol id="bat-critical" viewBox="0 0 30 12"><rect x="0.6" y="0.6" width="26" height="10.8" rx="2" fill="#fff" stroke="#222" stroke-width="1.2"/><rect x="27" y="3.5" width="2.5" height="5" fill="#222"/><g fill="#c0262c"><rect x="3" y="2.5" width="3.6" height="7"/><rect x="8" y="2.5" width="3.6" height="7"/><rect x="13" y="2.5" width="3.6" height="7"/><rect x="18" y="2.5" width="3.6" height="7"/><rect x="22.2" y="2.5" width="2.4" height="7"/></g></symbol>
    <symbol id="bat-high" viewBox="0 0 30 12"><rect x="0.6" y="0.6" width="26" height="10.8" rx="2" fill="#fff" stroke="#222" stroke-width="1.2"/><rect x="27" y="3.5" width="2.5" height="5" fill="#222"/><g fill="#ee7b22"><rect x="3" y="2.5" width="3.6" height="7"/><rect x="8" y="2.5" width="3.6" height="7"/><rect x="13" y="2.5" width="3.6" height="7"/><rect x="18" y="2.5" width="3.6" height="7"/></g></symbol>
    <symbol id="bat-medium" viewBox="0 0 30 12"><rect x="0.6" y="0.6" width="26" height="10.8" rx="2" fill="#fff" stroke="#222" stroke-width="1.2"/><rect x="27" y="3.5" width="2.5" height="5" fill="#222"/><g fill="#f3c51b"><rect x="3" y="2.5" width="3.6" height="7"/><rect x="8" y="2.5" width="3.6" height="7"/><rect x="13" y="2.5" width="3.6" height="7"/></g></symbol>
    <symbol id="bat-low" viewBox="0 0 30 12"><rect x="0.6" y="0.6" width="26" height="10.8" rx="2" fill="#fff" stroke="#222" stroke-width="1.2"/><rect x="27" y="3.5" width="2.5" height="5" fill="#222"/><g fill="#3fae3f"><rect x="3" y="2.5" width="3.6" height="7"/><rect x="8" y="2.5" width="3.6" height="7"/></g></symbol>
  </defs>
</svg>

<!-- Cover -->
<section class="page cover" style="left:13px;top:34px;padding:0">
  <div class="cover-logo"><i></i>PROBEWORKS</div>
  <h1>Engagement Title</h1>
  <div class="client">Client Name</div>
  <div class="date">January 17, 2018</div>
  <div class="art" role="img" aria-label="Line illustration of a gear, laptop with padlock, circuit traces and a phone"></div>
</section>
<div class="cover-band"></div>

<!-- Contents -->
<section class="page toc" style="left:315px;top:34px">
  <div class="brand"><i></i>PROBEWORKS</div><div class="pnum">1</div>
  <h2 class="left">Table of Contents</h2>
  <ul>
    <li>Engagement Title<span class="dots"></span>0</li>
    <li>Engagement Overview<span class="dots"></span>2</li>
    <li class="l2">Engagement Scope<span class="dots"></span>2</li>
    <li class="l2">Engagement Summary<span class="dots"></span>2</li>
    <li class="l2">Key Observations<span class="dots"></span>2</li>
    <li>Technical Overview<span class="dots"></span>3</li>
    <li class="l2">Severity Ratings<span class="dots"></span>3</li>
    <li class="l3 sub">Critical<span class="dots"></span>3</li>
    <li class="l3 sub">High<span class="dots"></span>3</li>
    <li class="l3 sub">Medium<span class="dots"></span>4</li>
    <li class="l3 sub">Low<span class="dots"></span>4</li>
    <li class="l2">Summary of Findings<span class="dots"></span>4</li>
    <li class="l2">Detailed Observations<span class="dots"></span>5</li>
    <li class="l3 b">Critical Findings<span class="dots"></span>5</li>
    <li class="l3">High Findings<span class="dots"></span>6</li>
    <li class="l3">Medium Findings<span class="dots"></span>7</li>
    <li class="l3">Low Findings<span class="dots"></span>8</li>
    <li>Concluding Remarks<span class="dots"></span>9</li>
    <li class="l2">Contact Information<span class="dots"></span>9</li>
  </ul>
  <div class="foot">CLIENT NAME</div>
</section>

<!-- Page 2 -->
<section class="page" style="left:618px;top:34px">
  <div class="brand"><i></i>PROBEWORKS</div><div class="pnum">2</div>
  <h2>Engagement Overview</h2>
  <p>Lorem ipsum dolor sit amet, consectetur adipiscing elit, sed do eiusmod tempor incididunt ut labore et dolore magna aliqua. Ut enim ad minim veniam, quis nostrud exercitation ullamco laboris nisi ut aliquip ex ea commodo consequat. Duis aute irure dolor in reprehenderit in voluptate velit esse cillum dolore eu fugiat nulla pariatur. Excepteur sint occaecat cupidatat non proident, sunt in culpa qui officia deserunt mollit anim id est laborum</p>
  <h3>Engagement Scope</h3>
  <p>Lorem ipsum dolor sit amet, consectetur adipiscing elit, sed do eiusmod tempor incididunt ut labore et dolore magna aliqua. Ut enim ad minim veniam, quis nostrud exercitation ullamco laboris nisi ut aliquip ex ea commodo consequat. Duis aute irure dolor in reprehenderit in voluptate velit esse cillum dolore eu fugiat nulla pariatur. Excepteur sint occaecat cupidatat non proident, sunt in culpa qui officia deserunt mollit anim id est laborum</p>
  <table class="data"><caption>Table 1</caption>
    <tr><td>Header 1</td><td>Header 2</td></tr>
    <tr><td>Target 1</td><td>Target 3</td></tr>
    <tr><td>Target 2</td><td>Target 4</td></tr>
  </table>
  <h3>Engagement Summary</h3>
  <p>Lorem ipsum dolor sit amet, consectetur adipiscing elit, sed do eiusmod tempor incididunt ut labore et dolore magna aliqua. Ut enim ad minim veniam, quis nostrud exercitation ullamco laboris nisi ut aliquip ex ea commodo consequat. Duis aute irure dolor in reprehenderit in voluptate velit esse cillum dolore eu fugiat nulla pariatur. Excepteur sint occaecat cupidatat non proident, sunt in culpa qui officia deserunt mollit anim id est laborum</p>
  <h3>Key Observations</h3>
  <p>Lorem ipsum dolor sit amet, consectetur adipiscing elit, sed do eiusmod tempor incididunt ut labore et dolore magna aliqua. Ut enim ad minim veniam, quis nostrud exercitation ullamco laboris nisi ut aliquip ex ea commodo consequat. Duis aute irure dolor in reprehenderit in voluptate velit esse cillum dolore</p>
  <div class="foot">CLIENT NAME</div>
</section>

<!-- Page 3 -->
<section class="page" style="left:920px;top:34px;padding-top:31px">
  <div class="brand"><i></i>PROBEWORKS</div><div class="pnum">3</div>
  <p>eu fugiat nulla pariatur. Excepteur sint occaecat cupidatat non proident, sunt in culpa qui officia deserunt mollit anim id est laborum</p>
  <table class="data"><caption>Table 2</caption>
    <tr><td>Header 1</td><td>Header 2</td></tr>
    <tr><td>Target 1</td><td>Target 3</td></tr>
    <tr><td>Target 2</td><td>Target 4</td></tr>
  </table>
  <h2 style="margin-top:12px">Technical Overview</h2>
  <p>Lorem ipsum dolor sit amet, consectetur adipiscing elit, sed do eiusmod tempor incididunt ut labore et dolore magna aliqua. Ut enim ad minim veniam, quis nostrud exercitation ullamco laboris nisi ut aliquip ex ea commodo consequat. Duis aute irure dolor in reprehenderit in voluptate velit esse cillum dolore eu fugiat nulla pariatur. Excepteur sint occaecat cupidatat non proident, sunt in culpa qui officia deserunt mollit anim id est laborum</p>
  <h3>Severity Ratings</h3>
  <div class="sev">Critical<svg width="24" height="10"><use href="#bat-critical"/></svg></div>
  <p>Duis aute irure dolor in reprehenderit in voluptate velit esse cillum dolore eu fugiat nulla pariatur. Excepteur sint occaecat cupidatat non proident, sunt in culpa qui officia deserunt mollit anim id est laborum</p>
  <div class="sev" style="margin-top:8px">High<svg width="24" height="10"><use href="#bat-high"/></svg></div>
  <p>Duis aute irure dolor in reprehenderit in voluptate velit esse cillum dolore eu fugiat nulla pariatur. Excepteur sint occaecat cupidatat non proident, sunt in culpa qui officia deserunt mollit anim id est laborum</p>
  <div class="foot">CLIENT NAME</div>
</section>

<!-- Page 4 -->
<section class="page" style="left:13px;top:423px;padding-top:31px">
  <div class="brand"><i></i>PROBEWORKS</div><div class="pnum">4</div>
  <div class="sev" style="margin-top:0">Medium<svg width="24" height="10"><use href="#bat-medium"/></svg></div>
  <p>Duis aute irure dolor in reprehenderit in voluptate velit esse cillum dolore eu fugiat nulla pariatur. Excepteur sint occaecat cupidatat non proident, sunt in culpa qui officia deserunt mollit anim id est laborum</p>
  <div class="sev" style="margin-top:8px">Low<svg width="24" height="10"><use href="#bat-low"/></svg></div>
  <p>Duis aute irure dolor in reprehenderit in voluptate velit esse cillum dolore eu fugiat nulla pariatur. Excepteur sint occaecat cupidatat non proident, sunt in culpa qui officia deserunt mollit anim id est laborum</p>
  <h3>Summary of Findings</h3>
  <p>Duis aute irure dolor in reprehenderit in voluptate velit esse cillum dolore eu fugiat nulla pariatur. Excepteur sint occaecat cupidatat non proident, sunt in culpa qui officia deserunt mollit anim id est laborum</p>
  <table class="data summary"><caption>Table 3</caption>
    <tr><th>Finding Name</th><th>Severity</th></tr>
    <tr><td>Critical Finding Title</td><td><svg width="28" height="11"><use href="#bat-critical"/></svg></td></tr>
    <tr><td>High Finding Title</td><td><svg width="28" height="11"><use href="#bat-high"/></svg></td></tr>
    <tr><td>Medium Finding Title</td><td><svg width="28" height="11"><use href="#bat-medium"/></svg></td></tr>
    <tr><td>Low Finding Title</td><td><svg width="28" height="11"><use href="#bat-low"/></svg></td></tr>
  </table>
  <div class="foot">CLIENT NAME</div>
</section>

<!-- Page 5 -->
<section class="page" style="left:315px;top:423px;padding:46px 0 0">
  <div class="brand"><i></i>PROBEWORKS</div><div class="pnum">5</div>
  <h2 style="margin-bottom:4px">Detailed Observations</h2>
  <table class="finding">
    <tr><th class="title" colspan="3">Critical Findings</th></tr>
    <tr><td class="issue" colspan="2">Insecure Configurations Identified</td><td class="icon"><svg width="28" height="11"><use href="#bat-critical"/></svg></td></tr>
    <tr><td class="k">Observation</td><td colspan="2">Lorem ipsum dolor sit amet, consectetur adipiscing elit, sed do eiusmod tempor incididunt ut labore et dolore magna aliqua. Ut enim ad minim veniam, quis nostrud exercitation ullamco laboris nisi ut aliquip ex ea commodo consequat.</td></tr>
    <tr><td class="k">Evidence</td><td colspan="2"><div class="shot" role="img" aria-label="Screenshot of the report document open in a word processor"></div><div class="caption">Caption:</div></td></tr>
    <tr><td class="k">Recommendation</td><td colspan="2">Lorem ipsum dolor sit amet, consectetur adipiscing elit, sed do eiusmod tempor incididunt ut labore et dolore magna aliqua. Ut enim ad minim veniam, quis nostrud exercitation ullamco laboris nisi ut aliquip ex ea commodo consequat.</td></tr>
    <tr><td class="k">Assets Affected</td><td colspan="2">127.0.0.1<br>127.0.0.2<br>127.0.0.3</td></tr>
  </table>
  <div class="foot">CLIENT NAME</div>
</section>

<!-- Page 6 -->
<section class="page" style="left:618px;top:423px;padding:41px 0 0">
  <div class="brand"><i></i>PROBEWORKS</div><div class="pnum">6</div>
  <table class="finding">
    <tr><th class="title" colspan="3">High Findings</th></tr>
    <tr><td class="issue" colspan="2">Insecure Configurations Identified</td><td class="icon"><svg width="28" height="11"><use href="#bat-high"/></svg></td></tr>
    <tr><td class="k">Observation</td><td colspan="2">Lorem ipsum dolor sit amet, consectetur adipiscing elit, sed do eiusmod tempor incididunt ut labore et dolore magna aliqua. Ut enim ad minim veniam, quis nostrud exercitation ullamco laboris nisi ut aliquip ex ea commodo consequat.</td></tr>
    <tr><td class="k">Evidence</td><td colspan="2"><div class="shot" role="img" aria-label="Screenshot of the report document open in a word processor"></div><div class="caption">Caption:</div></td></tr>
    <tr><td class="k">Recommendation</td><td colspan="2">Lorem ipsum dolor sit amet, consectetur adipiscing elit, sed do eiusmod tempor incididunt ut labore et dolore magna aliqua. Ut enim ad minim veniam, quis nostrud exercitation ullamco laboris nisi ut aliquip ex ea commodo consequat.</td></tr>
    <tr><td class="k">Assets Affected</td><td colspan="2">127.0.0.1<br>127.0.0.2<br>127.0.0.3</td></tr>
  </table>
  <div class="foot">CLIENT NAME</div>
</section>

<!-- Page 7 -->
<section class="page" style="left:920px;top:423px;padding:41px 0 0">
  <div class="brand"><i></i>PROBEWORKS</div><div class="pnum">7</div>
  <table class="finding">
    <tr><th class="title" colspan="3">Medium Findings</th></tr>
    <tr><td class="issue" colspan="2">Insecure Configurations Identified</td><td class="icon"><svg width="28" height="11"><use href="#bat-medium"/></svg></td></tr>
    <tr><td class="k">Observation</td><td colspan="2">Lorem ipsum dolor sit amet, consectetur adipiscing elit, sed do eiusmod tempor incididunt ut labore et dolore magna aliqua. Ut enim ad minim veniam, quis nostrud exercitation ullamco laboris nisi ut aliquip ex ea commodo consequat.</td></tr>
    <tr><td class="k">Evidence</td><td colspan="2"><div class="shot" role="img" aria-label="Screenshot of the report document open in a word processor"></div><div class="caption">Caption:</div></td></tr>
    <tr><td class="k">Recommendation</td><td colspan="2">Lorem ipsum dolor sit amet, consectetur adipiscing elit, sed do eiusmod tempor incididunt ut labore et dolore magna aliqua. Ut enim ad minim veniam, quis nostrud exercitation ullamco laboris nisi ut aliquip ex ea commodo consequat.</td></tr>
    <tr><td class="k">Assets Affected</td><td colspan="2">127.0.0.1<br>127.0.0.2<br>127.0.0.3</td></tr>
  </table>
  <div class="foot">CLIENT NAME</div>
</section>

<!-- Page 8 -->
<section class="page" style="left:13px;top:812px;padding:41px 0 0">
  <div class="brand"><i></i>PROBEWORKS</div><div class="pnum">8</div>
  <table class="finding">
    <tr><th class="title" colspan="3">Low Findings</th></tr>
    <tr><td class="issue" colspan="2">Insecure Configurations Identified</td><td class="icon"><svg width="28" height="11"><use href="#bat-low"/></svg></td></tr>
    <tr><td class="k">Observation</td><td colspan="2">Lorem ipsum dolor sit amet, consectetur adipiscing elit, sed do eiusmod tempor incididunt ut labore et dolore magna aliqua. Ut enim ad minim veniam, quis nostrud exercitation ullamco laboris nisi ut aliquip ex ea commodo consequat.</td></tr>
    <tr><td class="k">Evidence</td><td colspan="2"><div class="shot" role="img" aria-label="Screenshot of the report document open in a word processor"></div><div class="caption">Caption:</div></td></tr>
    <tr><td class="k">Recommendation</td><td colspan="2">Lorem ipsum dolor sit amet, consectetur adipiscing elit, sed do eiusmod tempor incididunt ut labore et dolore magna aliqua. Ut enim ad minim veniam, quis nostrud exercitation ullamco laboris nisi ut aliquip ex ea commodo consequat.</td></tr>
    <tr><td class="k">Assets Affected</td><td colspan="2">127.0.0.1<br>127.0.0.2<br>127.0.0.3</td></tr>
  </table>
  <div class="foot">CLIENT NAME</div>
</section>

<!-- Page 9 -->
<section class="page" style="left:315px;top:812px">
  <div class="brand"><i></i>PROBEWORKS</div><div class="pnum">9</div>
  <h2>Concluding Remarks</h2>
  <p>Duis aute irure dolor in reprehenderit in voluptate velit esse cillum dolore eu fugiat nulla pariatur. Excepteur sint occaecat cupidatat non proident, sunt in culpa qui officia deserunt mollit anim id est laborum</p>
  <h3 class="dark">Contact Information</h3>
  <p>Duis aute irure dolor in reprehenderit in voluptate velit esse cillum dolore eu fugiat nulla pariatur. Excepteur sint occaecat cupidatat non proident, sunt in culpa qui officia deserunt mollit anim id est laborum</p>
  <div class="foot">CLIENT NAME</div>
</section>

</body>
</html>
```